Quorvex business card design

create modern and tech looking business card that is clean but effectively communciates that we are a cloud communications company.
Should have at minimum:
Employee Name
Postion
Phone Number
Email
website
create modern and tech looking business card that is clean but effectively communciates that we are a cloud communications company. We have two logo color schemes (attached) so would like to see designs both ways
Should have at minimum:
Employee Name
Postion
Phone Number
Email
website

```html
<!DOCTYPE html>
<html lang="en">
<head>
<meta charset="utf-8">
<title>Quorvex business card</title>
<link rel="stylesheet" href="https://fonts.googleapis.com/css2?family=Exo+2:wght@400;500;700&display=swap">
<style>
  :root {
    --purple: #652d91;
    --purple-light: #7a44a6;
    --cyan: #2bb8e0;
    --ink: #3a3a3c;
    --paper: #ffffff;
    --backdrop: #e4e4e6;
  }
  * { margin: 0; padding: 0; box-sizing: border-box; }
  html, body { width: 1200px; height: 800px; overflow: hidden; }
  body {
    background: var(--backdrop);
    font-family: "Exo 2", sans-serif;
    position: relative;
  }
  .card {
    position: absolute;
    top: 250px;
    width: 520px;
    height: 300px;
    overflow: hidden;
    box-shadow: 0 10px 28px rgba(0,0,0,0.18);
  }
  .card--front { left: 40px; background: var(--paper); }
  .card--back {
    left: 640px;
    background: radial-gradient(circle at 45% 40%, var(--purple-light), var(--purple) 70%);
  }
  .card__band { position: absolute; inset: 0; }
  .person { position: absolute; left: 30px; top: 30px; }
  .person__name {
    color: var(--purple);
    font-weight: 700;
    font-size: 24px;
    letter-spacing: 1px;
  }
  .person__role {
    color: var(--cyan);
    font-size: 14px;
    letter-spacing: 0.5px;
  }
  .brand {
    position: absolute;
    display: flex;
    align-items: center;
    gap: 10px;
    font-weight: 700;
    letter-spacing: 2px;
  }
  .brand__mark { display: block; }
  .card--front .brand { left: 290px; top: 125px; color: var(--ink); font-size: 30px; }
  .card--front .brand__mark { width: 18px; height: 18px; background: var(--cyan); }
  .card--back .brand { left: 50%; top: 105px; transform: translateX(-50%); color: var(--paper); font-size: 44px; }
  .card--back .brand__mark { width: 24px; height: 24px; background: var(--cyan); }
  .contact {
    position: absolute;
    list-style: none;
    color: var(--paper);
    font-size: 14px;
    letter-spacing: 0.5px;
  }
  .contact li { display: flex; align-items: center; gap: 8px; margin-bottom: 5px; }
  .contact svg { width: 14px; height: 14px; flex: none; }
  .contact--personal { left: 30px; top: 165px; }
  .contact--web { right: 28px; top: 236px; }
  .site-url {
    position: absolute;
    left: 0; right: 0; top: 195px;
    text-align: center;
    color: var(--paper);
    font-size: 18px;
    letter-spacing: 1px;
  }
</style>
</head>
<body>

<section class="card card--front" aria-label="Card front">
  <svg class="card__band" viewBox="0 0 520 300" role="img" aria-label="Stepped purple band with soft pixel squares">
    <polygon fill="var(--purple)" points="0,135 120,135 120,110 175,110 175,170 215,170 215,205 300,205 300,245 345,245 345,220 400,220 400,232 520,232 520,300 0,300"/>
    <rect x="0" y="268" width="520" height="8" fill="var(--cyan)"/>
    <rect x="0" y="276" width="520" height="24" fill="var(--paper)"/>
  </svg>

  <div class="person">
    <p class="person__name">ELIAS MARDEN</p>
    <p class="person__role">Managing Director</p>
  </div>

  <div class="brand"><span class="brand__mark"></span>QUORVEX</div>

  <ul class="contact contact--personal">
    <li>
      <svg viewBox="0 0 14 14"><rect width="14" height="14" fill="var(--paper)"/><path d="M4 3h2l1 2.5-1.2.8a6 6 0 0 0 2 2l.8-1.2L11 8v2a1 1 0 0 1-1 1A7 7 0 0 1 3 4a1 1 0 0 1 1-1z" fill="var(--purple)"/></svg>
      888-415-0273
    </li>
    <li>
      <svg viewBox="0 0 14 14"><rect width="14" height="14" fill="var(--paper)"/><rect x="2.5" y="4" width="9" height="6.5" fill="none" stroke="var(--purple)" stroke-width="1.2"/><path d="M2.5 4l4.5 3.5L11.5 4" fill="none" stroke="var(--purple)" stroke-width="1.2"/></svg>
      elias@quorvex.com
    </li>
  </ul>

  <ul class="contact contact--web">
    <li>
      <svg viewBox="0 0 14 14"><rect width="14" height="14" fill="var(--paper)"/><circle cx="7" cy="7" r="4.5" fill="none" stroke="var(--purple)" stroke-width="1.1"/><ellipse cx="7" cy="7" rx="2" ry="4.5" fill="none" stroke="var(--purple)" stroke-width="1"/><line x1="2.5" y1="7" x2="11.5" y2="7" stroke="var(--purple)" stroke-width="1"/></svg>
      www.quorvex.com
    </li>
  </ul>
</section>

<section class="card card--back" role="img" aria-label="Card back: purple field with faint pixel squares">
  <div class="brand"><span class="brand__mark"></span>QUORVEX</div>
  <p class="site-url">www.quorvex.com</p>
</section>

</body>
</html>
```